VelaMend Wellness Business Cards

I am looking to have luxury business cards made for my IV Therapy and Wellness business.

Target Market(s)

Health and Wellness professionals

Industry/Entity Type

MedSpa

Contact Information for Business Card

Tobin Hargreave, MSN, RN, CCRN Tobin@velamendwellness.com (916) 582-1937 QR code to website www.velamendwellness.com

```html
<!DOCTYPE html>
<html lang="en">
<head>
<meta charset="UTF-8">
<title>VelaMend Wellness Business Cards</title>
<link href="https://fonts.googleapis.com/css2?family=Montserrat:wght@400;500;700&display=swap" rel="stylesheet">
<style>
  :root {
    --bg: #1f1f21;
    --navy-deep: #03064a;
    --navy-light: #3f3f7e;
    --navy-ink: #2b2f6b;
    --gold: #b89245;
    --sky: #2f9ee0;
    --paper: #ffffff;
    --ink: #222233;
    --muted: #444455;
  }
  * { margin: 0; padding: 0; box-sizing: border-box; }
  html, body { width: 1200px; height: 875px; overflow: hidden; }
  body {
    background: var(--bg);
    font-family: "Montserrat", sans-serif;
    position: relative;
  }
  .card {
    position: absolute;
    top: 288px;
    width: 520px;
    height: 300px;
    border-radius: 18px;
    overflow: hidden;
  }

  /* Front */
  .card-front {
    left: 50px;
    background: linear-gradient(120deg, var(--navy-light) 0%, #1c1d62 35%, var(--navy-deep) 65%);
    display: flex;
    align-items: center;
    justify-content: center;
  }
  .front-brand { text-align: center; color: var(--gold); }
  .front-brand .brand-mark {
    width: 22px; height: 22px; border-radius: 50%;
    background: var(--gold); margin: 0 auto 14px;
  }
  .front-brand .brand-name { font-size: 40px; font-weight: 500; letter-spacing: 1px; }
  .front-brand .brand-rule { height: 1.5px; background: var(--gold); width: 300px; margin: 12px auto 0; }

  /* Back */
  .card-back { left: 630px; background: var(--paper); color: var(--ink); }
  .back-brand-gold {
    position: absolute; right: 34px; top: 24px;
    color: var(--gold); font-size: 20px; font-weight: 500;
  }
  .back-brand-navy {
    position: absolute; right: 34px; top: 60px;
    display: flex; align-items: center; gap: 10px;
    color: var(--navy-ink); font-size: 28px; font-weight: 700;
  }
  .back-brand-navy .brand-dot { width: 14px; height: 14px; border-radius: 50%; background: var(--sky); }

  .person { position: absolute; left: 34px; top: 114px; }
  .person-name { font-size: 24px; font-weight: 700; color: var(--navy-ink); line-height: 30px; }
  .person-title { font-size: 12px; color: var(--muted); line-height: 16px; margin-top: 2px; }

  .divider { position: absolute; left: 34px; right: 34px; top: 170px; height: 1px; background: var(--navy-ink); }

  .contacts { position: absolute; left: 34px; top: 184px; list-style: none; }
  .contacts li {
    display: flex; align-items: center; gap: 8px;
    font-size: 12.5px; line-height: 24px; color: var(--ink);
  }
  .contacts svg { width: 12px; height: 12px; flex: none; }

  .address {
    position: absolute; right: 34px; top: 184px;
    font-size: 12px; line-height: 18px; text-align: right; color: var(--ink);
  }
  .qr-slot {
    position: absolute; right: 34px; bottom: 22px;
    width: 48px; height: 48px;
    background: var(--navy-ink); border-radius: 3px;
  }
</style>
</head>
<body>
  <section class="card card-front" aria-label="Card front">
    <div class="front-brand">
      <div class="brand-mark"></div>
      <div class="brand-name">VelaMend Wellness</div>
      <div class="brand-rule"></div>
    </div>
  </section>

  <section class="card card-back" aria-label="Card back">
    <div class="back-brand-gold">VelaMend Wellness</div>
    <div class="back-brand-navy"><span class="brand-dot"></span>VelaMend Wellness</div>

    <div class="person">
      <div class="person-name">Tobin Hargreave</div>
      <div class="person-title">MSN, RN, CCRN</div>
    </div>
    <div class="divider"></div>

    <ul class="contacts">
      <li>
        <svg viewBox="0 0 12 12"><rect x="3" y="0.5" width="6" height="11" rx="1.2" fill="none" stroke="#b89245" stroke-width="1.2"/></svg>
        (916) 582-1937
      </li>
      <li>
        <svg viewBox="0 0 12 12"><rect x="0.5" y="2" width="11" height="8" fill="none" stroke="#b89245" stroke-width="1.2"/><path d="M0.5 2 L6 7 L11.5 2" fill="none" stroke="#b89245" stroke-width="1.2"/></svg>
        Tobin@velamendwellness.com
      </li>
      <li>
        <svg viewBox="0 0 12 12"><circle cx="6" cy="6" r="5.2" fill="none" stroke="#b89245" stroke-width="1.2"/><path d="M1 6 H11 M6 1 C3 4 3 8 6 11 M6 1 C9 4 9 8 6 11" fill="none" stroke="#b89245" stroke-width="1"/></svg>
        www.velamendwellness.com
      </li>
    </ul>

    <div class="address">48 Alder Row, Suite<br>210, Easton, MA 02375</div>
    <div class="qr-slot" role="img" aria-label="QR code linking to www.velamendwellness.com"></div>
  </section>
</body>
</html>
```